Renew plant-based protein powder label

I would like a redesign for my current protein powder label . The current label idea should not be altered too much, but the design should be taken to the next level. Keep in mind that is should remain professional, not too extravagant. The main color for this label should remain red, because I represent each of my products with a specific color. It would be nice if a subtle (green) touch could be implemented to represent the plant based protein.

The logo should not be altered, and I prefer designs in Adobe Indesign (so I can adjust minor things if necessary later on).
Updates

Some adjustments to my project description: I generally like the idea of my current label but think that it can be uplifted even more. For instance, I like the idea of the hexagon structures as it is now, but it can be done better (try to create a 'wow-effect'). This does not mean that I exclude any other ideas, but they should be really good as otherwise it does not make any sense switching my entire product line to the new label format. The leaf picture that I included is not mandatory to use (as I have seen this a lot). I think the way in which Design #51394062 presented the bottom information (nr. of doses etc.) is creative. But as I mentioned, I intend to adjust the whole product line to this format so it has to be really good. Thanks a lot for your efforts and I look forward to new creativity.

Target Market(s)

Fitness market. usual customer is aged 18-25.

Industry/Entity Type

Fitness. Weight lifting.

Other font styles liked:
• See fonts attached that I use now. Use no script fonts.

Colors
00AB8E
00BBA5
67D7C9
C6EFE9
E9F9F6
EB3D1F
EC4F4E
F09395
F8D3D4
FCEDEE

Requirements
Must have
• The current design idea implemented.
Nice to have
• A subtle, but creative element of the plant-based aspect. Try to keep the main color red.
Should not have
• Extravagant designs

```html
<!DOCTYPE html>
<html lang="en">
<head>
<meta charset="utf-8">
<title>Ferro Nutrition – Pure Cacao Plant Protein Label</title>
<link rel="stylesheet" href="https://fonts.googleapis.com/css2?family=Montserrat:wght@300;400;700;800&display=swap">
<style>
  :root {
    --page-bg: #ffffff;
    --label-dark: #4b4649;
    --label-dark-deep: #3a3638;
    --hex-tone: #5a4a4c;
    --brand-white: #ffffff;
    --red-start: #d24a36;
    --red-end: #e04a4c;
    --teal-band: #5fc4b8;
    --teal-light: #78d2c7;
    --text-white: #ffffff;
  }
  html, body {
    margin: 0;
    padding: 0;
    width: 1200px;
    height: 1200px;
    overflow: hidden;
    background: var(--page-bg);
    font-family: "Montserrat", Arial, sans-serif;
  }
  .canvas {
    position: relative;
    width: 1200px;
    height: 1200px;
  }
  .label {
    position: absolute;
    left: 100px;
    top: 200px;
    width: 1000px;
    height: 800px;
    overflow: hidden;
    border-radius: 6px;
  }
  .label-pattern {
    position: absolute;
    inset: 0 0 170px 0;
    background:
      radial-gradient(ellipse at 50% 45%, var(--hex-tone) 0%, var(--label-dark) 55%, var(--label-dark-deep) 100%);
  }
  .brand {
    position: absolute;
    left: 170px;
    top: 250px;
    display: flex;
    align-items: center;
    gap: 28px;
    color: var(--brand-white);
    font-weight: 300;
  }
  .brand-mark {
    width: 46px;
    height: 46px;
    border-radius: 50%;
    background: var(--brand-white);
    flex: none;
  }
  .brand-name {
    margin: 0;
    font-size: 84px;
    line-height: 1;
    letter-spacing: 4px;
    font-weight: 300;
  }
  .brand-name span { display: block; }
  .flavour {
    position: absolute;
    left: 50%;
    top: 555px;
    transform: translateX(-50%);
    width: 470px;
    height: 70px;
    border-radius: 10px;
    background: linear-gradient(90deg, var(--red-start), var(--red-end));
    box-shadow: 0 3px 8px rgba(0,0,0,0.3);
    display: flex;
    align-items: center;
    justify-content: center;
    color: var(--text-white);
    font-weight: 800;
    font-size: 48px;
    letter-spacing: 1px;
    z-index: 2;
  }
  .info-band {
    position: absolute;
    left: 0;
    right: 0;
    bottom: 0;
    height: 220px;
    background: linear-gradient(90deg, var(--teal-band), var(--teal-light));
    color: var(--text-white);
  }
  .product-type {
    position: absolute;
    top: 48px;
    width: 100%;
    text-align: center;
    margin: 0;
    font-weight: 300;
    font-size: 50px;
    letter-spacing: 2px;
  }
  .pack-facts {
    position: absolute;
    left: 30px;
    right: 30px;
    top: 132px;
    display: flex;
    justify-content: space-between;
    font-weight: 700;
    font-size: 34px;
  }
</style>
</head>
<body>
  <main class="canvas">
    <section class="label">
      <div class="label-pattern" role="img" aria-label="Dark grey hexagon honeycomb pattern with faint red outlines"></div>

      <div class="brand">
        <div class="brand-mark"></div>
        <h1 class="brand-name"><span>FERRO</span><span>NUTRITION</span></h1>
      </div>

      <div class="flavour">Pure Cacao</div>

      <div class="info-band">
        <p class="product-type">Plant Protein</p>
        <div class="pack-facts">
          <span class="pack-weight">1.000 Gram</span>
          <span class="pack-servings">33 Servings</span>
        </div>
      </div>
    </section>
  </main>
</body>
</html>
```